Brindle Barks Chews Pouch Design

I want a pouch design for my yak cheese dog chews. My competitor is golden tail, see attached. I want something minimalist like that where you see that there is only 3 ingredients, Yak milk, lime juice, Himalayan salt. I want it to say 100% natural 100% organic on it. Also odor free. There has to be a big see through window on it so you can see the products inside. Here is my logo and my competitor package. The package is 13cm x 17cm x 5cm. I have 5 sizes of bags to create but same image design

Target Market(s)

Pet owners

Industry/Entity Type

Dog products

Requirements
Must have
• « SMALL » « MIN NET WT 200 g / 5 PCS » and its important the 3 ingredients mentioned and 100% natural and organic must be very visible however the window must be big
Should not have
• The ingredients in the back

```html
<!DOCTYPE html>
<html lang="en">
<head>
<meta charset="utf-8">
<title>Brindle Barks Chews – Pouch</title>
<link href="https://fonts.googleapis.com/css2?family=Montserrat:wght@800&family=Oswald:wght@500&display=swap" rel="stylesheet">
<style>
  :root {
    --stage: #2f2a1b;
    --pouch-orange: #f5a12a;
    --cream: #f7f2de;
    --maroon: #5e1b24;
    --chew-light: #e9a43c;
    --chew-dark: #b8641f;
    --sky: #6fb3d6;
    --mascot-brown: #b8742c;
  }
  html, body {
    margin: 0;
    width: 1200px;
    height: 731px;
    overflow: hidden;
    background: var(--stage);
  }
  .canvas {
    position: relative;
    width: 1200px;
    height: 731px;
  }
  .pouch {
    position: absolute;
    left: 350px;
    top: 40px;
    width: 500px;
    height: 650px;
  }
  .label-bold {
    font-family: "Montserrat", sans-serif;
    font-weight: 800;
  }
  .ingredients {
    font-family: "Oswald", sans-serif;
    font-weight: 500;
    font-size: 29px;
    fill: var(--maroon);
  }
</style>
</head>
<body>
<div class="canvas">
  <svg class="pouch" viewBox="0 0 500 650" xmlns="http://www.w3.org/2000/svg">
    <defs>
      <linearGradient id="window-fill" x1="0" y1="0" x2="1" y2="0">
        <stop offset="0" stop-color="var(--chew-light)"/>
        <stop offset="0.5" stop-color="var(--chew-dark)"/>
        <stop offset="0.75" stop-color="#9c2f22"/>
        <stop offset="1" stop-color="var(--chew-light)"/>
      </linearGradient>
      <linearGradient id="mascot-fill" x1="0" y1="0" x2="0" y2="1">
        <stop offset="0" stop-color="var(--sky)"/>
        <stop offset="0.55" stop-color="var(--mascot-brown)"/>
        <stop offset="1" stop-color="#6e9a3e"/>
      </linearGradient>
      <path id="ingredient-curve" d="M30,512 C170,512 330,470 482,428"/>
      <path id="badge-natural-top" d="M272,112 A40,40 0 0 1 352,112"/>
      <path id="badge-natural-bottom" d="M268,112 A44,44 0 0 0 356,112"/>
      <path id="badge-odor-top" d="M382,108 A40,40 0 0 1 462,108"/>
      <path id="badge-odor-bottom" d="M378,108 A44,44 0 0 0 466,108"/>
    </defs>

    <rect class="pouch-body" x="0" y="0" width="500" height="650" rx="6" fill="var(--pouch-orange)"/>
    <rect class="hang-slot" x="215" y="22" width="70" height="12" rx="6" fill="#c97d17"/>
    <rect class="hang-slot-tab" x="240" y="14" width="20" height="12" rx="4" fill="#c97d17"/>

    <path class="cream-frame" d="M0,150 C120,60 320,150 500,60 L500,480 C370,480 230,550 0,555 Z" fill="var(--cream)"/>

    <path class="product-window" role="img" aria-label="See-through window showing the yak milk chews inside"
      d="M22,200 C150,150 330,200 478,128 L478,395 C350,420 210,470 22,470 Z" fill="url(#window-fill)"/>

    <circle class="mascot-art" role="img" aria-label="Brand mascot illustration with mountain scenery" cx="125" cy="135" r="78" fill="url(#mascot-fill)"/>

    <g class="brand-plate">
      <rect x="8" y="224" width="234" height="74" rx="10" fill="var(--cream)"/>
      <text class="brand-name label-bold" x="125" y="256" text-anchor="middle" font-size="25" fill="var(--maroon)" textLength="214" lengthAdjust="spacingAndGlyphs">BRINDLE BARKS</text>
      <text class="brand-name label-bold" x="125" y="287" text-anchor="middle" font-size="25" fill="var(--maroon)">CHEWS</text>
    </g>

    <g class="badge-natural">
      <circle cx="312" cy="112" r="52" fill="var(--cream)" stroke="var(--maroon)" stroke-width="4"/>
      <circle cx="312" cy="112" r="30" fill="none" stroke="var(--maroon)" stroke-width="3"/>
      <text class="label-bold" font-size="10" fill="var(--maroon)"><textPath href="#badge-natural-top" startOffset="50%" text-anchor="middle">100% NATURAL</textPath></text>
      <text class="label-bold" font-size="10" fill="var(--maroon)"><textPath href="#badge-natural-bottom" startOffset="50%" text-anchor="middle" dominant-baseline="hanging">100% ORGANIC</textPath></text>
      <path d="M312,128 C300,112 302,100 312,94 C322,100 324,112 312,128 Z M312,128 L312,100" fill="var(--maroon)" stroke="var(--cream)" stroke-width="1.5"/>
    </g>

    <g class="badge-odor">
      <circle cx="422" cy="108" r="52" fill="var(--cream)" stroke="var(--maroon)" stroke-width="4"/>
      <circle cx="422" cy="108" r="30" fill="none" stroke="var(--maroon)" stroke-width="3"/>
      <text class="label-bold" font-size="10" fill="var(--maroon)"><textPath href="#badge-odor-top" startOffset="50%" text-anchor="middle">ODOR FREE</textPath></text>
      <text class="label-bold" font-size="10" fill="var(--maroon)"><textPath href="#badge-odor-bottom" startOffset="50%" text-anchor="middle" dominant-baseline="hanging">ODOR FREE</textPath></text>
      <path d="M416,126 C406,116 426,108 416,96 M428,126 C418,116 438,108 428,96" fill="none" stroke="var(--maroon)" stroke-width="4" stroke-linecap="round"/>
      <line x1="402" y1="128" x2="442" y2="88" stroke="var(--maroon)" stroke-width="4" stroke-linecap="round"/>
    </g>

    <text class="ingredients"><textPath href="#ingredient-curve" textLength="440" lengthAdjust="spacingAndGlyphs">Yak Milk • Lime Juice • Himalayan Salt</textPath></text>

    <g class="weight-band">
      <path d="M0,570 L232,562 L228,594 L0,602 Z" fill="var(--maroon)"/>
      <text class="label-bold" x="40" y="588" font-size="15" fill="var(--cream)">MIN NET WT 200g</text>
    </g>
    <g class="size-tag">
      <path d="M236,562 L336,556 L332,588 L232,594 Z" fill="var(--cream)"/>
      <text class="label-bold" x="284" y="582" text-anchor="middle" font-size="16" fill="var(--maroon)">SMALL</text>
    </g>
    <g class="count-seal">
      <circle cx="398" cy="572" r="50" fill="var(--cream)"/>
      <circle cx="398" cy="572" r="44" fill="var(--maroon)"/>
      <text class="label-bold" x="398" y="580" text-anchor="middle" font-size="46" fill="var(--cream)">5</text>
      <text class="label-bold" x="398" y="602" text-anchor="middle" font-size="13" fill="var(--cream)">PCS</text>
    </g>
  </svg>
</div>
</body>
</html>
```